Cover für Erstlingswerk
Ich habe von Quorel ein phantastisches Cover für mein Buch bekommen. Ganz anders als ich es mir bei Auftragsstellung vorgestellt habe. Sehr innovativ und außergewöhnlich. Die Zusammenarbeit war freundlich und locker, spontan und flexibel. Ich bedanke mich ganz herzlich für dieses wundervolle Cover für mein Herzensprojekt!
Zielgruppe
Es handelt sich um einen Roman, der insbesondere Frauen zwischen 30 und 60 Jahren ansprechen wird.
Aufgabenstellung
Das Cover soll schlicht, ohne Schnörkel sein, bevorzugte Farben blau wie die Nordsee und der Himmel, grün und braun wie der Kiefernwald und das Dünengras und weiß wie die Wolken. Ggf. ein Bezug zu Dänemark. Aber ich bin für alle Ideen offen.
Noch ein Nachtrag: dies ist mein erster Auftrag und mein erstes Buch, daher, wenn es Fragen gibt, bitte stellen. Ich habe auch einen Klappentext, wird der zu diesem Zeitpunkt schon eingebunden? Es steckt viel Herzblut und Zeit in meinem ersten Roman. Wenn ich für das Cover mehr Input geben soll, bitte mitteilen!
Noch ein Nachtrag: Der Titel des Buches lautet "Morgen wird es hell" und der Name der Autorin Petra Wolters.

```html
<!DOCTYPE html>
<html lang="de">
<head>
<meta charset="utf-8">
<title>Morgen wird es hell – Buchcover</title>
<link rel="stylesheet" href="https://fonts.googleapis.com/css2?family=Dancing+Script:wght@400;500&family=Philosopher&family=Delius&display=swap">
<style>
  :root {
    --stage: #b9c2c4;
    --sand: #e8e3d8;
    --sand-light: #efebe2;
    --ink: #4a6670;
    --ink-soft: #55707a;
    --white: #ffffff;
  }
  * { margin: 0; padding: 0; box-sizing: border-box; }
  html, body { width: 1200px; height: 800px; overflow: hidden; }
  body {
    background: linear-gradient(180deg, #a9b3b6 0%, var(--stage) 70%, #c6cdce 100%);
    position: relative;
  }
  .cover {
    position: absolute;
    top: 100px;
    height: 600px;
    background: linear-gradient(180deg, var(--sand-light), var(--sand));
    box-shadow: 0 10px 30px rgba(40, 55, 60, 0.25);
    overflow: hidden;
  }
  .cover--front { left: 190px; width: 390px; }
  .cover--back { left: 592px; width: 390px; }
  .cover--spine { left: 982px; width: 40px; }

  .surf { position: absolute; top: 0; left: 0; width: 100%; height: 120px; }

  .author {
    position: absolute;
    top: 112px; left: 0; width: 100%;
    text-align: center;
    font-family: "Philosopher", sans-serif;
    font-size: 36px;
    color: var(--ink);
    letter-spacing: 0.5px;
  }
  .photo {
    position: absolute;
    border-radius: 110px 110px 0 0;
  }
  .photo--front {
    left: 50px; top: 165px; width: 210px; height: 435px;
    background: linear-gradient(180deg, #2a3c4a 0%, #4f6a7a 35%, #6a8a90 62%, #5f8580 80%, #3a4c44 100%);
  }
  .photo--back {
    left: 120px; top: 440px; width: 150px; height: 160px;
    border-radius: 75px 75px 0 0;
    background: linear-gradient(180deg, #2a3c4a 0%, #5f7886 45%, #6f9595 75%, #3a4c44 100%);
  }

  .title {
    position: absolute;
    font-family: "Dancing Script", cursive;
    color: var(--white);
    text-align: center;
    line-height: 1;
  }
  .title span { display: block; }
  .title--front { left: 45px; top: 250px; width: 220px; font-size: 58px; }
  .title--front span + span { margin-top: 22px; }
  .title--front .title__last { font-size: 88px; margin-top: 16px; }
  .title--back { left: 110px; top: 478px; width: 170px; font-size: 30px; }
  .title--back span + span { margin-top: 8px; }
  .title--back .title__last { font-size: 42px; margin-top: 6px; }

  .genre {
    position: absolute;
    left: 276px; top: 492px;
    font-family: "Philosopher", sans-serif;
    font-size: 24px;
    color: var(--ink);
  }

  .blurb-quote {
    position: absolute;
    left: 32px; top: 150px; width: 316px;
    font-family: "Dancing Script", cursive;
    font-size: 19px;
    line-height: 1.55;
    color: var(--ink-soft);
    text-align: justify;
    text-align-last: justify;
  }
  .blurb {
    position: absolute;
    left: 32px; top: 222px; width: 316px;
    font-family: "Delius", sans-serif;
    font-size: 11.6px;
    line-height: 1.72;
    color: var(--ink-soft);
    text-align: justify;
  }
  .spine-text {
    position: absolute;
    left: 50%; top: 0;
    width: 600px; height: 40px;
    transform-origin: 0 0;
    transform: rotate(90deg) translate(0, -50%);
    display: flex; align-items: center; justify-content: space-between;
    padding: 0 30px;
    white-space: nowrap;
    color: var(--ink);
  }
  .spine-text__title { font-family: "Dancing Script", cursive; font-size: 26px; }
  .spine-text__author { font-family: "Philosopher", sans-serif; font-size: 11px; opacity: 0.7; }
</style>
</head>
<body>

<section class="cover cover--front">
  <svg class="surf" viewBox="0 0 390 120" preserveAspectRatio="none" role="img" aria-label="Foto: Brandung am Sandstrand von oben">
    <defs>
      <linearGradient id="surfFront" x1="0" y1="0" x2="0" y2="1">
        <stop offset="0" stop-color="#bcdbd6"/>
        <stop offset="0.6" stop-color="#dfe9e3"/>
        <stop offset="1" stop-color="#f1efe8"/>
      </linearGradient>
    </defs>
    <path d="M0 0 H390 V55 C330 60 300 95 250 100 C200 104 170 80 120 78 C70 76 30 85 0 90 Z" fill="url(#surfFront)"/>
  </svg>

  <p class="author">Petra Wolters</p>

  <div class="photo photo--front" role="img" aria-label="Foto: Silhouette einer Frau im Profil, gefüllt mit Wolkenhimmel und Nordsee"></div>

  <h1 class="title title--front">
    <span>Morgen</span>
    <span>wird es</span>
    <span class="title__last">hell</span>
  </h1>

  <p class="genre">Roman</p>
</section>

<section class="cover cover--back">
  <svg class="surf" viewBox="0 0 390 120" preserveAspectRatio="none" role="img" aria-label="Foto: Brandung am Sandstrand von oben">
    <defs>
      <linearGradient id="surfBack" x1="0" y1="0" x2="0" y2="1">
        <stop offset="0" stop-color="#c3e0de"/>
        <stop offset="0.6" stop-color="#e1ebe6"/>
        <stop offset="1" stop-color="#f1efe8"/>
      </linearGradient>
    </defs>
    <path d="M0 0 H390 V60 C350 62 320 70 290 90 C250 110 210 112 170 92 C130 72 90 70 40 76 C20 78 8 80 0 82 Z" fill="url(#surfBack)"/>
  </svg>

  <p class="blurb-quote">Als ich erwachte, musste ich wieder an<br>das Haus denken, dieses alte Haus.</p>

  <p class="blurb">Hanne ist am Ende ihrer Kräfte und fühlt sich von den Menschen in ihrer Umgebung im Stich gelassen. Selbst ihr Lebensgefährte Lars und das ländlich gelegene Haus mit dem großen Garten können nicht mehr davon ablenken, dass sie zutiefst unglücklich ist. Da führt sie ein Zufall und die vergessene Schulfreundin Simone nach Jütland an die dänische Nordsee, wo ihr neben dem rauen Meer insbesondere der alte Fischer Leif Mut macht, endlich sie selbst zu sein.</p>

  <div class="photo photo--back" role="img" aria-label="Foto: kleine Silhouette einer Frau im Profil mit Himmel und Meer"></div>

  <p class="title title--back">
    <span>Morgen</span>
    <span>wird es</span>
    <span class="title__last">hell</span>
  </p>
</section>

<section class="cover cover--spine">
  <div class="spine-text">
    <span class="spine-text__title">Morgen wird es hell</span>
    <span class="spine-text__author">Petra Wolters</span>
  </div>
</section>

</body>
</html>
```